GRAPHIC DESIGN FOR RESTAURANT MENU FOR HEALTHY RESTAURANT

I am looking for a graphic design for our menu displayed on a TV screen. Please ensure the file will fit on a TV screen nicely. We are looking for a clean design , with the following items. We would also like to include a couple of photos.
Breakfast:
Protein Chocolate Chip Pancakes - $12.95
Dawn Hustle Burrito- $11.95
Hearty Harvest Omelette - $12.95
Lunch
Butter Chicken - $13.95
Chicken Quesadilla - $13.45
Coconut Garlic Shrimp - $15.95
Goat Cheese Stuffed Chicken - $14.95
Chipotle Steak Wrap - $12.95
Turkey Meatball Fettuccini - $13.45
Chicken Alfredo - $13.45
Chicken Parmesan - $13.95
Pesto Chicken Pasta - $13.45
Steak Bite and Green Stir Fry - $13.45
Asian Chicken Teriyaki - $13.45
Please include our logo

```html
<!DOCTYPE html>
<html lang="en">
<head>
<meta charset="utf-8">
<title>Greenfork Menu Board</title>
<link href="https://fonts.googleapis.com/css2?family=Alegreya:wght@700;900&family=Kaushan+Script&family=Montserrat:wght@400;800&display=swap" rel="stylesheet">
<style>
  :root {
    --bg-page: #e9e6e1;
    --board: #1f1f20;
    --board-mid: #2b2b2c;
    --green: #8cc63f;
    --green-deep: #6fa82a;
    --white: #ffffff;
    --ink: #141414;
    --plate: #efe9df;
  }
  * { margin: 0; padding: 0; box-sizing: border-box; }
  html, body { width: 1200px; height: 967px; overflow: hidden; background: var(--bg-page); }
  .menu-board {
    position: absolute; left: 0; top: 146px; width: 1200px; height: 675px;
    background: radial-gradient(ellipse at 55% 50%, var(--board-mid), var(--board) 75%);
    overflow: hidden; font-family: "Alegreya", Georgia, serif; color: var(--white);
  }
  .board-shapes { position: absolute; inset: 0; }
  .brand {
    position: absolute; left: 740px; top: 38px; width: 440px; height: 64px;
    display: flex; align-items: center; justify-content: center; gap: 14px;
  }
  .brand-dot { width: 20px; height: 20px; border-radius: 50%; background: var(--green-deep); }
  .brand-name {
    font-family: "Montserrat", Arial, sans-serif; font-weight: 800; font-size: 50px;
    letter-spacing: 2px; color: var(--green-deep); line-height: 1;
  }
  .title-script {
    position: absolute; left: 120px; top: 270px; font-family: "Kaushan Script", cursive;
    font-size: 92px; color: var(--green); line-height: 1.1; white-space: nowrap;
  }
  .title-sub {
    position: absolute; left: 92px; top: 378px; font-family: "Montserrat", Arial, sans-serif;
    font-weight: 400; font-size: 44px; letter-spacing: 2px; color: var(--white); line-height: 1;
  }
  .section-label {
    position: absolute; font-family: "Kaushan Script", cursive; font-size: 34px;
    color: var(--ink); line-height: 1; text-align: center;
  }
  .section-label.breakfast { left: 612px; width: 336px; top: 198px; }
  .section-label.lunch { left: 96px; width: 276px; top: 435px; }
  .item-list { position: absolute; list-style: none; }
  .item-list li {
    display: flex; justify-content: space-between; align-items: baseline;
    font-weight: 700; font-size: 17px; height: 33px; white-space: nowrap;
  }
  .item-list .price { font-weight: 900; font-size: 21px; color: var(--green); }
  .list-breakfast { left: 624px; top: 262px; width: 440px; }
  .list-lunch-a { left: 108px; top: 495px; width: 336px; }
  .list-lunch-b { left: 516px; top: 452px; width: 324px; }
  .plate-photo { position: absolute; border-radius: 4px; }
  .plate-pancake { left: 856px; top: 318px; width: 104px; height: 44px;
    background: linear-gradient(180deg, #a0734a, var(--plate)); }
  .plate-omelette { left: 462px; top: 366px; width: 150px; height: 56px;
    background: linear-gradient(180deg, #8a6a4a, #e2b758 55%, var(--plate)); }
</style>
</head>
<body>
<main class="menu-board">
  <svg class="board-shapes" width="1200" height="675" viewBox="0 0 1200 675">
    <defs>
      <radialGradient id="wrap-tone" cx="50%" cy="70%" r="60%">
        <stop offset="0" stop-color="#b4693b"/>
        <stop offset="1" stop-color="#d9c2a0"/>
      </radialGradient>
      <radialGradient id="pasta-tone" cx="40%" cy="40%" r="65%">
        <stop offset="0" stop-color="#c8402a"/>
        <stop offset="1" stop-color="#e0a66a"/>
      </radialGradient>
    </defs>
    <circle cx="250" cy="-170" r="445" fill="none" stroke="var(--white)" stroke-width="2"/>
    <circle cx="250" cy="-170" r="422" fill="var(--green)"/>
    <circle cx="250" cy="-170" r="400" fill="var(--white)"/>
    <circle cx="250" cy="-170" r="392" fill="url(#wrap-tone)" role="img" aria-label="Photo of a sliced steak and vegetable wrap"/>
    <circle cx="1130" cy="640" r="266" fill="none" stroke="var(--white)" stroke-width="2"/>
    <circle cx="1130" cy="640" r="246" fill="var(--green)"/>
    <circle cx="1130" cy="640" r="228" fill="var(--white)"/>
    <circle cx="1136" cy="640" r="220" fill="url(#pasta-tone)" role="img" aria-label="Photo of turkey meatballs over fettuccini with tomato sauce and cheese"/>
    <path d="M712 34 L1200 14 L1200 112 L722 124 L734 100 L700 88 L726 72 L704 54 Z" fill="var(--white)"/>
    <path d="M616 196 L940 186 L956 200 L942 214 L952 232 L622 244 L604 232 L618 220 L606 208 Z" fill="var(--green)"/>
    <path d="M100 434 L364 428 L378 440 L366 452 L374 468 L106 476 L92 464 L102 452 L90 444 Z" fill="var(--green)"/>
  </svg>

  <div class="brand">
    <span class="brand-dot"></span>
    <span class="brand-name">GREENFORK</span>
  </div>

  <div class="title-script">Menú</div>
  <div class="title-sub">RESTAURANT</div>

  <div class="section-label breakfast">Breakfast:</div>
  <ul class="item-list list-breakfast">
    <li><span>Protein Chocolate Chip Pancakes</span><span class="price">$12.95</span></li>
    <li><span>Dawn Hustle Burrito</span><span class="price">$11.95</span></li>
    <li><span>Hearty Harvest Omelette</span><span class="price">$12.95</span></li>
  </ul>

  <div class="plate-photo plate-pancake" role="img" aria-label="Photo of chocolate chip pancakes on a white plate"></div>
  <div class="plate-photo plate-omelette" role="img" aria-label="Photo of an omelette with toast on a white plate"></div>

  <div class="section-label lunch">Lunch</div>
  <ul class="item-list list-lunch-a">
    <li><span>Butter Chicken</span><span class="price">$13.95</span></li>
    <li><span>Chicken Quesadilla</span><span class="price">$13.45</span></li>
    <li><span>Coconut Garlic Shrimp</span><span class="price">$15.95</span></li>
    <li><span>Goat Cheese Stuffed Chicken</span><span class="price">$14.95</span></li>
    <li><span>Chipotle Steak Wrap</span><span class="price">$12.95</span></li>
  </ul>
  <ul class="item-list list-lunch-b">
    <li><span>Turkey Meatball Fettuccini</span><span class="price">$13.45</span></li>
    <li><span>Chicken Alfredo</span><span class="price">$13.45</span></li>
    <li><span>Chicken Parmesan</span><span class="price">$13.95</span></li>
    <li><span>Pesto Chicken Pasta</span><span class="price">$13.45</span></li>
    <li><span>Steak Bite and Green Stir Fry</span><span class="price">$13.45</span></li>
    <li><span>Asian Chicken Teriyaki</span><span class="price">$13.45</span></li>
  </ul>
</main>
</body>
</html>
```